Namecard Designs+Logo for a High End Automobile Company

We need a new business card for our company called Velta Motorhof.

www.veltamotorhof.example.sg
Our new website will be up in 2.5 months time.

We sell used and brand new continental cars like Korvane, QTL, Dravell, Solbrini and etc. Currently we are operating from 2 offices in Singapore and United Kingdom.

We want a design which is serious. We are open to colours but try to keep it at a maximum of 3 colours.

We prefer something simple and minimal. We are open to 2 sides printing or even 2 sided namecards. Both UK and Singapore company offices address must be in; either side by side, front and back, or even 2 sided cards.

The logo can be a text logo, emblem, abstract, pictorial or combination.

We are printing with Pribo.com so please kindly follow the printing guideline.

http://uk.pribo.example/help/faq/templates-and-guidelines.html

Rich and Car Enthusiasts

Printing

Must have
• Our 2 offices; UK and Singapore.

Our slogan which is " The Automobile Specialist"
Should not have
• Not more than 3 colours

```html
<!DOCTYPE html>
<html lang="en">
<head>
<meta charset="UTF-8">
<title>Velta Motorhof — Business Card</title>
<link rel="stylesheet" href="https://fonts.googleapis.com/css2?family=Montserrat:wght@600&family=Open+Sans:wght@400;600;700&display=swap">
<style>
  :root {
    --page: #ffffff;
    --card: #0c0a0a;
    --copper: #c0824c;
    --white: #ffffff;
    --slogan-grey: #8d8c8c;
    --panel-top: #3b3939;
    --panel-bottom: #161414;
    --car-light: #4a4848;
    --car-dark: #121010;
  }
  * { margin: 0; padding: 0; box-sizing: border-box; }
  html, body {
    width: 1200px;
    height: 900px;
    overflow: hidden;
    background: var(--page);
  }
  .business-card {
    position: absolute;
    left: 146px;
    top: 170px;
    width: 914px;
    height: 550px;
    background: var(--card);
    overflow: hidden;
    font-family: "Open Sans", Arial, sans-serif;
  }
  .brand {
    position: absolute;
    left: 0;
    top: 64px;
    width: 540px;
    text-align: center;
  }
  .brand-mark {
    display: block;
    width: 26px;
    height: 26px;
    margin: 0 auto 30px;
    background: var(--copper);
  }
  .brand-name {
    font-family: "Montserrat", Arial, sans-serif;
    font-weight: 600;
    font-size: 37px;
    letter-spacing: 1px;
    color: var(--white);
    text-transform: uppercase;
    line-height: 1;
  }
  .slogan {
    margin-top: 30px;
    font-weight: 700;
    font-size: 31px;
    line-height: 37px;
    color: var(--slogan-grey);
  }
  .website {
    margin-top: 22px;
    font-weight: 700;
    font-size: 22px;
    color: var(--copper);
  }
  .offices {
    position: absolute;
    left: 544px;
    top: 44px;
    width: 352px;
    height: 310px;
    padding-top: 18px;
    background: linear-gradient(to bottom, var(--panel-top), var(--panel-bottom));
    text-align: center;
    color: var(--white);
  }
  .office + .office { margin-top: 18px; }
  .office-name {
    font-weight: 700;
    font-size: 23px;
    color: var(--copper);
    line-height: 30px;
    margin-bottom: 4px;
  }
  .office-line {
    font-size: 24px;
    line-height: 32px;
  }
  .car-visual {
    position: absolute;
    left: 44px;
    top: 370px;
    width: 870px;
    height: 200px;
    border-radius: 320px 420px 0 0 / 120px 160px 0 0;
    background: radial-gradient(ellipse at 55% 30%, var(--car-light), var(--car-dark) 70%);
  }
</style>
</head>
<body>
  <div class="business-card">
    <div class="car-visual" role="img" aria-label="Side view of a black sports car along the bottom of the card"></div>

    <div class="brand">
      <span class="brand-mark"></span>
      <div class="brand-name">Velta Motorhof</div>
      <div class="slogan">The Automobile<br>Specialist</div>
      <div class="website">www.veltamotorhof.example.sg</div>
    </div>

    <div class="offices">
      <div class="office">
        <div class="office-name">United Kingdom</div>
        <div class="office-line">Address line</div>
        <div class="office-line">P: 0000000</div>
        <div class="office-line">E: email address line</div>
      </div>
      <div class="office">
        <div class="office-name">Singapore</div>
        <div class="office-line">Address line</div>
        <div class="office-line">P: 0000000</div>
        <div class="office-line">E: email address line</div>
      </div>
    </div>
  </div>
</body>
</html>
```